Brindle Finance Flyer Design

I would like a high res flyer designed for mass printing. It is for a mortgage and finance broking company in Sydney. We are called Brindle Finance. The wording i would like displayed is the following
Looking For Something Extra from your broker?
Brindle Finance can make all the difference
What we offer you is an extensive range of mortgage and finance products, including:
• Home Loans
• Investment Loans
• Low Doc Loans
• Vehicle Finance
• Equipment Finance
• Commercial Loans
• Refinance
Contact Us
Phone (02) 7412 5830
email info@brindlefinance.com.au
web www.brindlefinance.com.au
Industry/Entity Type
Finance
Look and feel

```html
<!DOCTYPE html>
<html lang="en">
<head>
<meta charset="utf-8">
<title>Brindle Finance Flyer</title>
<link rel="stylesheet" href="https://fonts.googleapis.com/css2?family=Arimo:wght@400;700&family=Open+Sans:wght@400;500&display=swap">
<style>
  :root {
    --white: #ffffff;
    --ink-grey: #4a4a4c;
    --contact-ink: #222222;
    --band-grey: #c9cbcd;
    --blue-deep: #0a86bd;
    --blue-mid: #1a9dd3;
    --blue-light: #3ab4e4;
    --photo-light: #eef3f8;
    --photo-mid: #c7d4e4;
    --photo-navy: #2c3b63;
  }
  * { margin: 0; padding: 0; box-sizing: border-box; }
  html, body { width: 927px; height: 1200px; overflow: hidden; background: var(--white); }
  .flyer { position: relative; width: 927px; height: 1200px; overflow: hidden; font-family: "Arimo", Arial, sans-serif; }

  .header { position: absolute; top: 0; left: 0; width: 927px; height: 165px; background: var(--white); }
  .brand { position: absolute; left: 38px; top: 52px; font-family: "Open Sans", Arial, sans-serif; color: var(--ink-grey); }
  .brand-name { display: flex; align-items: center; gap: 14px; font-size: 58px; font-weight: 400; line-height: 1; letter-spacing: -0.5px; }
  .brand-square { width: 48px; height: 48px; background: var(--ink-grey); flex: none; }
  .brand-tagline { margin-top: 6px; margin-left: 62px; font-size: 19px; font-weight: 400; letter-spacing: 0.1px; }

  .contact { position: absolute; right: 39px; top: 52px; text-align: right; font-size: 16.5px; line-height: 21.5px; color: var(--contact-ink); }

  .band { position: absolute; left: 0; width: 927px; height: 9px; background: var(--band-grey); }
  .band-top { top: 165px; }
  .band-bottom { top: 624px; }

  .hero-photo { position: absolute; top: 174px; left: 0; width: 927px; height: 450px;
    background: linear-gradient(90deg, var(--photo-light) 0%, var(--photo-mid) 35%, var(--photo-light) 50%, var(--photo-navy) 68%, var(--photo-navy) 78%, var(--photo-light) 90%, var(--photo-light) 100%); }

  .offer { position: absolute; top: 633px; left: 0; width: 927px; height: 567px; color: var(--white);
    background: linear-gradient(160deg, var(--blue-mid) 0%, var(--blue-deep) 45%, var(--blue-light) 100%); }
  .offer-question { position: absolute; top: 60px; width: 100%; text-align: center; font-size: 27px; font-weight: 700; }
  .offer-headline { position: absolute; top: 118px; width: 100%; text-align: center; font-size: 37px; font-weight: 700; letter-spacing: 0.3px; }
  .offer-divider { position: absolute; top: 206px; left: 200px; }
  .offer-intro { position: absolute; top: 262px; width: 100%; text-align: center; font-size: 22px; font-weight: 700; line-height: 29px; color: #eaf6fc; }
  .product-list { position: absolute; top: 364px; list-style: none; font-size: 25px; font-weight: 700; line-height: 33px; }
  .product-list li::before { content: "• "; }
  .product-list-left { left: 100px; }
  .product-list-right { left: 556px; }
</style>
</head>
<body>
<div class="flyer">
  <header class="header">
    <div class="brand">
      <div class="brand-name"><span class="brand-square"></span>Brindle Finance</div>
      <div class="brand-tagline">mortgage and finance broking services</div>
    </div>
    <address class="contact" style="font-style:normal">
      <div>Contact Us</div>
      <div>Phone (02) 7412 5830</div>
      <div>email info@brindlefinance.com.au</div>
      <div>web www.brindlefinance.com.au</div>
    </address>
  </header>

  <div class="band band-top"></div>
  <div class="hero-photo" role="img" aria-label="Blurred business people walking through a bright modern office corridor"></div>
  <div class="band band-bottom"></div>

  <section class="offer">
    <p class="offer-question">Looking For Something Extra from your broker?</p>
    <h1 class="offer-headline">Brindle Finance can make all the difference!</h1>
    <svg class="offer-divider" width="527" height="4" viewBox="0 0 527 4" aria-hidden="true">
      <defs>
        <linearGradient id="divider-fade" x1="0" x2="1" y1="0" y2="0">
          <stop offset="0" stop-color="#ffffff" stop-opacity="0"/>
          <stop offset="0.5" stop-color="#ffffff" stop-opacity="0.85"/>
          <stop offset="1" stop-color="#ffffff" stop-opacity="0"/>
        </linearGradient>
      </defs>
      <rect width="527" height="4" fill="url(#divider-fade)"/>
    </svg>
    <p class="offer-intro">What we offer you is an extensive range of mortgage<br>and finance products, including:</p>
    <ul class="product-list product-list-left">
      <li>Home Loans</li>
      <li>Investment Loans</li>
      <li>Low Doc Loans</li>
      <li>Vehicle Finance</li>
    </ul>
    <ul class="product-list product-list-right">
      <li>Equipment Finance</li>
      <li>Commercial Loans</li>
      <li>Refinance</li>
    </ul>
  </section>
</div>
</body>
</html>
```